Marchesi Orthodontics
Business Card / Stationary Design
Professional
Lucia Marchesi
Orthodontist
4817 W. Harborview Ave. Suite 204
Fort Lauderdale, FL 33419
marchesiortho@mailvexo.com
www.pinegrovesmiles.com

```html
<!DOCTYPE html>
<html lang="en">
<head>
<meta charset="utf-8">
<title>Marchesi Orthodontics — Stationery</title>
<link href="https://fonts.googleapis.com/css2?family=Open+Sans:wght@400;600&display=swap" rel="stylesheet">
<style>
  :root {
    --backdrop: #e9e6e1;
    --paper: #ffffff;
    --brand-blue: #1b8fd6;
    --deep-blue: #0c4fa8;
    --mid-blue: #2f7fe0;
    --ink: #4a4f57;
    --ink-soft: #8a9098;
    --rule: #d4d8de;
  }
  * { margin: 0; padding: 0; box-sizing: border-box; }
  html, body { width: 1200px; height: 886px; overflow: hidden; }
  body {
    position: relative;
    background: var(--backdrop);
    font-family: "Open Sans", Arial, sans-serif;
    color: var(--ink);
  }
  .piece {
    position: absolute;
    background: var(--paper);
    box-shadow: 0 2px 6px rgba(0,0,0,.18);
  }
  .brand-name {
    font-family: "Open Sans", Arial, sans-serif;
    font-weight: 600;
    color: var(--brand-blue);
    line-height: 1.2;
    white-space: nowrap;
  }

  /* Business card — contact side */
  .card-details { left: 197px; top: 24px; width: 230px; height: 130px; border-radius: 10px; }
  .card-details .info { position: absolute; left: 108px; top: 20px; font-size: 5.4px; line-height: 1.5; color: var(--ink); }
  .card-details .person { font-weight: 600; font-size: 6.4px; color: var(--deep-blue); }
  .card-details .role { margin-bottom: 6px; color: var(--ink-soft); }
  .card-details .block { margin-bottom: 4px; }

  /* Business card — blue brand side */
  .card-blue {
    left: 79px; top: 170px; width: 226px; height: 130px; border-radius: 10px;
    background: radial-gradient(ellipse at 50% 50%, #3e8ff0 0%, var(--mid-blue) 35%, var(--deep-blue) 100%);
    display: flex; align-items: center; justify-content: center;
  }
  .card-blue .brand-name { color: #ffffff; font-size: 14px; }

  /* Business card — white brand side */
  .card-white {
    left: 319px; top: 170px; width: 228px; height: 130px; border-radius: 10px;
    display: flex; align-items: center; justify-content: center;
  }
  .card-white .brand-name { font-size: 14px; }

  /* Envelope front */
  .envelope-front { left: 29px; top: 314px; width: 571px; height: 269px; padding: 28px 18px; }
  .envelope-front .brand-name { font-size: 18px; }
  .envelope-front .return {
    position: absolute; left: 18px; bottom: 18px;
    font-size: 6px; line-height: 1.6; color: var(--ink-soft);
  }

  /* Envelope back */
  .envelope-back { left: 29px; top: 598px; width: 571px; height: 252px; }
  .envelope-back svg { position: absolute; inset: 0; }
  .envelope-back .flap-mark {
    position: absolute; left: 0; right: 0; top: 58px;
    text-align: center; font-size: 10px;
  }

  /* Letterhead */
  .letterhead { left: 636px; top: 29px; width: 540px; height: 823px; }
  .letterhead .brand-name { position: absolute; right: 86px; top: 122px; font-size: 20px; }
  .letterhead .footer {
    position: absolute; left: 60px; right: 60px; bottom: 38px;
    border-top: 1px solid var(--rule); padding-top: 8px;
    text-align: right; font-size: 6.4px; line-height: 1.6; color: var(--ink-soft);
  }
</style>
</head>
<body>

  <section class="piece card-details" aria-label="Business card, contact side">
    <div class="info">
      <div class="person">Lucia Marchesi, D.M.D., M.S.</div>
      <div class="role">Orthodontist</div>
      <div class="block">4817 W. Harborview Ave. Suite 204<br>Fort Lauderdale, FL 33419</div>
      <div class="block">P: 954.555.0142<br>F: 954.555.0143</div>
      <div>marchesiortho@mailvexo.com<br>www.pinegrovesmiles.com</div>
    </div>
  </section>

  <section class="piece card-blue" aria-label="Business card, brand side on blue">
    <div class="brand-name">Marchesi Orthodontics</div>
  </section>

  <section class="piece card-white" aria-label="Business card, brand side on white">
    <div class="brand-name">Marchesi Orthodontics</div>
  </section>

  <section class="piece envelope-front" aria-label="Envelope front">
    <div class="brand-name">Marchesi Orthodontics</div>
    <div class="return">
      4817 W. Harborview Ave. Suite 204 Fort Lauderdale, FL 33419<br>
      P 954.555.0142 | F 954.555.0143 | marchesiortho@mailvexo.com | www.pinegrovesmiles.com
    </div>
  </section>

  <section class="piece envelope-back" aria-label="Envelope back">
    <svg width="571" height="252" viewBox="0 0 571 252" fill="none" stroke="#c9cdd3" stroke-width="1">
      <path d="M0 0 L255 92 Q285.5 104 316 92 L571 0"/>
      <path d="M0 252 L236 128 Q285.5 108 335 128 L571 252"/>
      <path d="M0 0 Q120 110 236 128"/>
      <path d="M571 0 Q451 110 335 128"/>
    </svg>
    <div class="brand-name flap-mark">Marchesi Orthodontics</div>
  </section>

  <section class="piece letterhead" aria-label="Letterhead">
    <div class="brand-name">Marchesi Orthodontics</div>
    <div class="footer">
      4817 W. Harborview Ave. Suite 204 Fort Lauderdale, FL 33419<br>
      P 954.555.0142 | F 954.555.0143 | marchesiortho@mailvexo.com | www.pinegrovesmiles.com
    </div>
  </section>

</body>
</html>
```